Website Redesign using existing images, copy etc.

I'm looking for a website redesign/refresh of my current WordPress website. I would like to utilize the same photography, a new photo viewer, and an overall refresh of the entire design. This will need to be WordPress with simple accessibility to make changes as we add additional properties and make updates. We auction luxury real estate and luxury yachts for non-distressed sellers. It needs to be simple, luxurious and with ease of use for both web and especially mobile. www.HarborCrestBids.com

```html
<!DOCTYPE html>
<html lang="en">
<head>
<meta charset="utf-8">
<title>HarborCrest Bids — Luxury Real Estate &amp; Yacht Auctions</title>
<link href="https://fonts.googleapis.com/css2?family=Crimson+Pro:wght@400;500;600&family=Montserrat:wght@400;500;600;700&family=Roboto:wght@700&display=swap" rel="stylesheet">
<style>
:root{
  --gold:#9a7b4f;
  --ink:#2b2b2b;
  --navy:#14263a;
  --sand:#efebe4;
  --pill:#cfc7b7;
  --press:#77716a;
  --footer:#4a4642;
  --footer-bar:#6a5e52;
  --footer-text:#e9e3d9;
  --white:#ffffff;
}
*{box-sizing:border-box;margin:0;padding:0}
html,body{width:1200px;height:2893px;overflow:hidden;background:var(--white)}
body{position:relative;font-family:"Montserrat",sans-serif;color:var(--ink)}
.abs{position:absolute}

.hero{left:0;top:0;width:1200px;height:492px;
  background:
    radial-gradient(ellipse 420px 220px at 780px 150px,rgba(196,140,70,.55),rgba(196,140,70,0) 70%),
    radial-gradient(ellipse 520px 260px at 260px 180px,rgba(210,205,195,.28),rgba(210,205,195,0) 70%),
    linear-gradient(180deg,#343a4c 0%,#4d4640 30%,#3f4433 58%,#2b3526 80%,#1f281c 100%)}
.nav-mark{left:113px;top:25px;width:40px;height:40px;border:2px solid var(--white);border-radius:50%}
.nav a{position:absolute;top:38px;color:var(--white);font-size:13px;text-decoration:none;letter-spacing:.3px}
.btn-outline{position:absolute;display:flex;align-items:center;justify-content:center;border:1px solid rgba(255,255,255,.8);border-radius:20px;color:var(--white);font-size:13px;letter-spacing:.3px}
.hero-btn{background:rgba(120,105,85,.55)}
.wordmark{left:560px;top:160px;width:526px;text-align:right;color:var(--white);font-family:"Crimson Pro",serif;font-size:38px;letter-spacing:8px;line-height:1;white-space:nowrap}
.tagline{left:760px;top:200px;width:316px;text-align:right;color:var(--white);font-size:13px;letter-spacing:4.5px}

.intro-card{left:112px;top:445px;width:974px;height:291px;background:var(--white);border-radius:0 0 22px 22px;box-shadow:0 8px 18px rgba(0,0,0,.08);text-align:center}
.intro-card h1{margin-top:60px;font-family:"Crimson Pro",serif;font-weight:400;font-size:30px;color:var(--ink)}
.intro-card h2{margin-top:10px;font-size:13px;font-weight:600;color:var(--gold)}
.intro-card p{margin:24px auto 0;width:770px;font-size:11.5px;line-height:14px}
.intro-dot{left:579px;top:657px;width:42px;height:42px;border:1.5px solid var(--gold);border-radius:50%}

.press-band{left:0;top:844px;width:1200px;height:330px;background:var(--sand)}
.press-label{left:470px;top:811px;width:260px;height:64px;background:var(--white);box-shadow:0 6px 14px rgba(0,0,0,.08);display:flex;align-items:center;justify-content:center;font-family:"Crimson Pro",serif;font-size:30px;color:var(--gold);letter-spacing:.5px}
.press-row{left:200px;top:920px;width:800px;height:84px}
.press-name{position:absolute;top:0;height:84px;display:flex;align-items:center;justify-content:center;text-align:center;font-family:"Crimson Pro",serif;font-weight:600;color:var(--press);font-size:23px;line-height:1}
.press-copy{left:212px;top:1048px;width:776px;text-align:center;font-size:11.5px;line-height:14px}
.pill-white{left:543px;top:1119px;width:136px;height:38px;background:var(--white);border-radius:20px;display:flex;align-items:center;justify-content:center;font-size:13px;box-shadow:0 3px 8px rgba(0,0,0,.08)}

.photo{border:1.5px solid var(--gold);border-radius:8px}
.photo-estate{left:157px;top:1258px;width:886px;height:499px;
  background:
    radial-gradient(ellipse 300px 260px at 460px 300px,rgba(160,110,50,.85),rgba(160,110,50,0) 75%),
    radial-gradient(ellipse 520px 120px at 560px 40px,rgba(150,105,55,.8),rgba(150,105,55,0) 80%),
    linear-gradient(180deg,#6a7784 0%,#3c5a78 35%,#2c4c6c 70%,#22405e 100%)}
.photo-porch{left:157px;top:2124px;width:886px;height:286px;
  background:
    radial-gradient(ellipse 260px 110px at 200px 230px,rgba(88,130,60,.95),rgba(88,130,60,0) 80%),
    linear-gradient(180deg,rgba(120,170,210,.9) 0%,rgba(200,215,225,.4) 45%,rgba(0,0,0,0) 60%),
    linear-gradient(90deg,#7ea7c9 0%,#6f9a5e 38%,#ebe6d8 52%,#d8cfbd 66%,#9c8d72 85%,#6e6250 100%)}
.story-card{left:112px;top:1579px;width:208px;height:238px;background:var(--white);border-radius:10px;box-shadow:0 6px 16px rgba(0,0,0,.1);text-align:center}
.story-card h3{margin-top:60px;font-family:"Roboto",sans-serif;font-weight:700;font-size:33px;line-height:46px;color:var(--navy);letter-spacing:-.5px}
.pill-gold{position:absolute;display:flex;align-items:center;justify-content:center;border:1px solid var(--gold);border-radius:18px;color:var(--gold);font-size:13px}
.about-copy{left:150px;top:1868px;width:900px;text-align:center;font-size:11.8px;line-height:14.2px}
.pill-sand{left:473px;top:2007px;width:254px;height:32px;background:var(--pill);border:1px solid #6b6255;border-radius:18px;display:flex;align-items:center;justify-content:center;font-size:13px;color:#4a4642}
.about-card{left:880px;top:2359px;width:206px;height:105px;background:var(--white);border-radius:10px;box-shadow:0 6px 16px rgba(0,0,0,.1);display:flex;align-items:center;justify-content:center;font-size:13px}

.footer{left:0;top:2513px;width:1200px;height:380px;background:var(--footer)}
.footer-bar{left:112px;top:2592px;width:977px;height:42px;background:var(--footer-bar);border-radius:6px}
.footer-label{position:absolute;top:2606px;color:var(--footer-text);font-size:13px;letter-spacing:.3px}
.social{position:absolute;top:2668px;width:25px;height:25px;border-radius:50%;background:#b5a383}
.badge{left:166px;top:2740px;width:56px;height:56px;border-radius:50%;background:#6f6354}
.badge-bar{left:157px;top:2800px;width:72px;height:16px;background:#6f6354;border-radius:3px}
.quick a{position:absolute;left:430px;color:var(--footer-text);font-size:14px;text-decoration:none}
.field{position:absolute;left:680px;width:409px;height:30px;border-bottom:1.5px solid #8a7f72;color:#b9afa2;font-size:11px;padding:8px 17px 0}
.submit{left:680px;top:2791px;width:86px;height:32px;background:#8a7f72;border:1px solid #b9afa2;border-radius:18px;color:var(--white);font-size:13px;display:flex;align-items:center;justify-content:center}
.footer-bottom{left:112px;top:2852px;width:977px;height:41px;background:var(--footer-bar);border-radius:6px 6px 0 0;color:var(--footer-text);font-size:11px}
.footer-bottom span{position:absolute;top:14px}
</style>
</head>
<body>

<div class="abs hero" role="img" aria-label="Hillside Mediterranean villa with lit windows and a pergola at dusk, surrounded by tall grasses"></div>
<div class="abs nav-mark"></div>
<nav class="nav">
  <span class="abs" style="left:647px;top:24px;width:4px;height:4px;border-radius:50%;background:#fff"></span>
  <a style="left:635px" href="#">BUY</a>
  <a style="left:700px" href="#">SELL</a>
  <a style="left:769px" href="#">ABOUT</a>
  <a style="left:855px" href="#">855-210-4417</a>
</nav>
<div class="btn-outline" style="left:988px;top:30px;width:98px;height:32px">CONTACT</div>

<div class="abs wordmark">HARBORCREST BIDS</div>
<div class="abs tagline">Real Estate &amp; Yachts</div>
<div class="btn-outline hero-btn" style="left:834px;top:252px;width:252px;height:32px">BROWSE UPCOMING AUCTIONS</div>
<div class="btn-outline hero-btn" style="left:853px;top:306px;width:216px;height:31px">BROWSE PAST SUCCESSES</div>

<section class="abs intro-card">
  <h1>Over One Billion Dollars of Auctions Marketed</h1>
  <h2>Real Estate &amp; Yachts</h2>
  <p>The experience of hearing the auctioneer’s final proclamation of “SOLD!” is unparalleled. Whether it’s the initial meeting with the seller at their estate or yacht, or the triumphant raising of the paddle by the winning buyer, we relish every moment of the process and the ensuing festivities. We’re confident that you will, too.</p>
</section>
<div class="abs intro-dot"></div>

<div class="abs press-band"></div>
<div class="abs press-label">As Featured In</div>
<div class="abs press-row">
  <span class="press-name" style="left:15px;width:110px">The Daily<br>Ledger</span>
  <span class="press-name" style="left:148px;width:120px">Capital<br>Weekly</span>
  <span class="press-name" style="left:295px;width:170px">Estate<br>Quarterly</span>
  <span class="press-name" style="left:515px;width:160px">Market<br>Channel</span>
  <span class="press-name" style="left:700px;width:95px">News<br>Hour</span>
</div>
<p class="abs press-copy">By offering top-tier properties and vessels globally, along with strategic auction dates, exceptional marketing tactics, and a diligent public relations team, even the most prominent media outlets have taken notice. Check out some of our latest press <b>features.</b></p>
<div class="abs pill-white">VIEW PRESS</div>

<div class="abs photo photo-estate" role="img" aria-label="Aerial view of a brick waterfront estate on a wooded peninsula with autumn trees and a stone shoreline"></div>
<div class="abs story-card">
  <h3>Grasonville<br>Maryland</h3>
</div>
<div class="pill-gold" style="left:135px;top:1753px;width:163px;height:31px">SUCCESSES STORY</div>

<p class="abs about-copy">HarborCrest Bids is a top-tier destination for luxury property auctions, having overseen the auction marketing of numerous high-end estates and yachts. Our team of luxury home auction experts is committed to helping property owners obtain the best value for their assets while ensuring a timely sale. Whether you have an expansive compound or a metropolitan penthouse, HarborCrest Bids has the necessary skills and expertise to facilitate various luxury real estate auctions. What’s even better? Our team takes care of every aspect of the process in cooperation with tour realtor/broker, including property tours, photography and cinematography, marketing advertising, public relations and more. Apart from high-end real estate auctions, we can also organize and execute luxury yacht auctions to help boat owners find qualified buyers for their vessels. Interested in finding out more about our luxury home and yacht auctions? Explore our current listings and<br><b>success stories!</b></p>
<div class="abs pill-sand">BROWSE&nbsp;<b>UPCOMING AUCTIONS</b></div>

<div class="abs photo photo-porch" role="img" aria-label="Beachfront porch with wicker seating and white columns overlooking palm trees and the ocean"></div>
<div class="abs about-card">LEARN MORE&nbsp;<b>ABOUT US</b></div>

<footer>
  <div class="abs footer"></div>
  <div class="abs footer-bar"></div>
  <span class="footer-label" style="left:157px">FOLLOW ALONG</span>
  <span class="footer-label" style="left:430px">QUICK LINKS</span>
  <span class="footer-label" style="left:680px">SIGN UP FOR HARBORCREST ALERTS</span>
  <span class="social" style="left:157px"></span>
  <span class="social" style="left:196px"></span>
  <span class="social" style="left:234px"></span>
  <span class="social" style="left:272px"></span>
  <div class="abs badge"></div>
  <div class="abs badge-bar"></div>
  <div class="quick">
    <a href="#" style="top:2651px">Home</a>
    <a href="#" style="top:2682px">Buy</a>
    <a href="#" style="top:2713px">Sell</a>
    <a href="#" style="top:2744px">About</a>
    <a href="#" style="top:2775px">Blog</a>
    <a href="#" style="top:2806px">Contact</a>
  </div>
  <div class="field" style="top:2676px">Name</div>
  <div class="field" style="top:2728px">Email</div>
  <div class="abs submit">SUBMIT</div>
  <div class="abs footer-bottom">
    <span style="left:45px">© Copyright Corwell 2023 All Right Reserved.</span>
    <span style="left:736px">Terms Of Use</span>
    <span style="left:824px;width:1px;height:14px;background:#e9e3d9;top:13px"></span>
    <span style="left:844px">Privacy Policy</span>
  </div>
</footer>

</body>
</html>
```